Business Card for Fashion House

We need a business card design for our personalize fashion service for our customers. the business card should reflect reliability, luxury and creativity.
The brand Gravetto is extracted from "Graceful Vetto"; Gravetto provides fashion designs sprinkled with luxury and style tailored for our elite clients character profile.
Gravetto is created for those who embody class and elegance with a passion for style.
Target Market(s)
Affluent Customers
Industry/Entity Type
Fashion
Contact Information for Business Card
Rania Bou Khalil
Fashion Designer
Telephone: +971 5550123
Mobile +971 555987
Emal q@z.com
Website www.gravetto-example.com
Social Media Youtube g+ Facebook Instagram Pin /gravetto
Font styles to use
Other font styles liked:
- Audrey provided
Look and feel
Each slider illustrates characteristics of the customer's brand and the style your logo design should communicate.

```html
<!DOCTYPE html>
<html lang="en">
<head>
<meta charset="utf-8">
<title>Gravetto – Business Card</title>
<link rel="stylesheet" href="https://fonts.googleapis.com/css2?family=Marcellus&family=Cormorant+Garamond:wght@500&display=swap">
<style>
  :root {
    --stage: #cbbfa9;
    --card-white: #ffffff;
    --card-white-fade: #ececec;
    --ink: #1a1a1a;
    --card-black: #0c0c0c;
    --card-black-soft: #1b1b1b;
    --paper-text: #f4f4f4;
  }
  * { margin: 0; padding: 0; box-sizing: border-box; }
  html, body { width: 1200px; height: 545px; overflow: hidden; }
  body { background: var(--stage); position: relative; }

  .card {
    position: absolute;
    top: 113px;
    width: 518px;
    height: 304px;
    box-shadow: 0 4px 10px rgba(0, 0, 0, 0.35);
  }

  /* Front */
  .card-front {
    left: 60px;
    background: linear-gradient(180deg, var(--card-white) 0%, var(--card-white) 55%, var(--card-white-fade) 100%);
    color: var(--ink);
  }
  .brand-mark {
    position: absolute;
    left: 0; width: 296px;
    top: 168px;
    text-align: center;
    font-family: "Marcellus", serif;
    font-size: 25px;
    letter-spacing: 0.32em;
    text-indent: 0.32em;
  }
  .social-handle {
    position: absolute;
    left: 0; width: 296px;
    top: 209px;
    display: flex;
    justify-content: center;
    align-items: center;
    gap: 8px;
    font-family: "Marcellus", serif;
    font-size: 13px;
    letter-spacing: 0.08em;
  }
  .social-handle .dot {
    width: 9px; height: 9px;
    border-radius: 50%;
    background: var(--ink);
  }
  .divider {
    position: absolute;
    left: 274px; top: 44px;
    width: 1px; height: 224px;
    background: var(--ink);
  }
  .person {
    position: absolute;
    left: 304px; top: 40px;
    font-family: "Marcellus", serif;
  }
  .person-name {
    font-size: 19px;
    letter-spacing: 0.14em;
    font-weight: 400;
  }
  .person-role {
    font-size: 12px;
    letter-spacing: 0.1em;
    margin-top: 3px;
  }
  .contact {
    position: absolute;
    left: 304px; top: 192px;
    list-style: none;
    font-family: "Cormorant Garamond", serif;
    font-weight: 500;
    font-size: 14px;
    line-height: 20px;
    letter-spacing: 0.04em;
  }

  /* Back */
  .card-back {
    left: 619px;
    background: linear-gradient(90deg, var(--card-black) 0%, var(--card-black-soft) 50%, var(--card-black) 100%);
    color: var(--paper-text);
  }
  .back-wordmark {
    position: absolute;
    left: 0; width: 100%;
    top: 186px;
    text-align: center;
    font-family: "Marcellus", serif;
    font-size: 23px;
    letter-spacing: 0.34em;
    text-indent: 0.34em;
  }
</style>
</head>
<body>
  <section class="card card-front">
    <div class="brand-mark">GRAVETTO</div>
    <div class="social-handle"><span class="dot"></span><span>gravetto</span></div>
    <div class="divider"></div>
    <div class="person">
      <h1 class="person-name">RANIA BOU KHALIL</h1>
      <p class="person-role">FASHION DESIGNER</p>
    </div>
    <ul class="contact">
      <li>P: +971 5550123</li>
      <li>M: +971 555987</li>
      <li>q@z.com</li>
      <li>www.gravetto-example.com</li>
    </ul>
  </section>

  <section class="card card-back" role="img" aria-label="Black card back with a faint repeating monogram pattern and the Gravetto name">
    <div class="back-wordmark">GRAVETTO</div>
  </section>
</body>
</html>
```